Hadley & Partners, LLC Business Card 2016

We need a new business card design for a very important trade show coming up.

We are a compliance Consulting Firm. Our clients are stock brokerage firms and investment advisers.

I would like our logo on both sides of the card.

Info in the front of the card shold include:

Logo
First & Last Name
Title
Office #
Cell #
Email
Company Address (42 W. Calloway St., Suite 300 Pasadena, CA 91417

Back of the card should include the logo and url: www.hadleypartnersgroup.com

Target Market(s)

Stock Brokerage Firms and Investment Advisers

Industry/Entity Type

Financial Service

Contact Information for Business Card

Marcus J. Pellew
President
42 W. Calloway St., Suite 300
Pasadena, CA 91417
O 626.555.0147 ext. 204
C 818.555.0193
Email: marcus@hadleypartnersgroup.com
www.hadleypartnersgroup.com

Requirements
Nice to have
• The back of the card could be black with the logo with the white letters.
• I do want the front of the card to at least have the color logo with the black "Hadley & Partners Lettering.

```html
<!DOCTYPE html>
<html lang="en">
<head>
<meta charset="utf-8">
<title>Hadley &amp; Partners — Business Card</title>
<link rel="stylesheet" href="https://fonts.googleapis.com/css2?family=Libre+Baskerville:wght@400;700&family=Arimo:wght@400&display=swap">
<style>
  :root {
    --canvas: #e9e9e9;
    --card-light: #f1f1f1;
    --card-dark: #262626;
    --ink: #1f1f1f;
    --ink-soft: #3a3a3a;
    --brand-red: #9b1c1c;
    --brand-red-bright: #c42222;
    --white: #ffffff;
  }
  * { box-sizing: border-box; margin: 0; padding: 0; }
  html, body { width: 1200px; height: 900px; overflow: hidden; }
  body {
    background: var(--canvas);
    font-family: "Arimo", Arial, sans-serif;
    display: flex;
    flex-direction: column;
    align-items: center;
    justify-content: center;
    gap: 24px;
  }
  .card {
    position: relative;
    width: 700px;
    height: 400px;
    box-shadow: 0 6px 18px rgba(0,0,0,0.12);
    overflow: hidden;
  }

  /* Front */
  .card--front { background: var(--card-light); color: var(--ink); }
  .contact-block { position: absolute; left: 330px; top: 58px; }
  .person-name {
    font-family: "Libre Baskerville", Georgia, serif;
    font-weight: 700;
    font-size: 22px;
    color: var(--brand-red);
  }
  .person-title { font-size: 16px; margin-top: 4px; color: var(--ink-soft); }
  .contact-list { list-style: none; margin-top: 36px; font-size: 16px; line-height: 23px; }
  .contact-list li { display: flex; align-items: center; gap: 10px; }
  .contact-list svg { width: 12px; height: 12px; fill: var(--brand-red-bright); flex: none; }
  .address { font-style: normal; margin-top: 28px; margin-left: 4px; font-size: 16px; line-height: 23px; }

  .wordmark {
    display: flex; align-items: center; gap: 10px;
    font-family: "Libre Baskerville", Georgia, serif;
    font-weight: 400;
    letter-spacing: 1px;
    text-transform: uppercase;
    white-space: nowrap;
  }
  .wordmark__square { background: var(--brand-red-bright); flex: none; }
  .card--front .wordmark {
    position: absolute; left: 36px; top: 318px;
    font-size: 15px; letter-spacing: 0.5px; gap: 8px; color: var(--ink);
  }
  .card--front .wordmark__square { width: 22px; height: 22px; }

  .footer-band {
    position: absolute; left: 0; right: 0; bottom: 0; height: 24px;
    background: var(--ink);
  }
  .footer-band::before, .footer-band::after {
    content: ""; position: absolute; bottom: 0; width: 28px; height: 24px;
    background: var(--brand-red);
  }
  .footer-band::before { left: 0; }
  .footer-band::after { right: 0; height: 30px; }

  /* Back */
  .card--back {
    background: var(--card-dark); color: var(--white);
    display: flex; flex-direction: column; align-items: center; justify-content: center;
    gap: 34px;
  }
  .card--back .wordmark { font-size: 34px; color: var(--white); }
  .card--back .wordmark__square { width: 44px; height: 44px; }
  .website { font-size: 18px; letter-spacing: 0.5px; }
</style>
</head>
<body>
  <section class="card card--front" aria-label="Card front">
    <div class="contact-block">
      <h1 class="person-name">Marcus J. Pellew</h1>
      <p class="person-title">President</p>
      <ul class="contact-list">
        <li>
          <svg viewBox="0 0 12 12" aria-hidden="true"><path d="M2.5 0.5 L4.5 3 L3.4 4.3 C4.2 6 5.9 7.7 7.7 8.6 L9 7.5 L11.5 9.5 L10.2 11.4 C5.5 11 1 6.5 0.6 1.8 Z"/></svg>
          626.555.0147 ext. 204
        </li>
        <li>
          <svg viewBox="0 0 12 12" aria-hidden="true"><path d="M3 0 H9 V12 H3 Z M4.2 1.4 V9.2 H7.8 V1.4 Z M5.4 10 H6.6 V11 H5.4 Z" fill-rule="evenodd"/></svg>
          818.555.0193
        </li>
        <li>
          <svg viewBox="0 0 12 12" aria-hidden="true"><path d="M0 2.5 H12 V10 H0 Z"/><path d="M0 2.5 L6 6.6 L12 2.5 V3.6 L6 7.8 L0 3.6 Z" fill="#f1f1f1"/></svg>
          marcus@hadleypartnersgroup.com
        </li>
      </ul>
      <address class="address">
        42 W. Calloway St.<br>
        Suite 300<br>
        Pasadena, CA 91417
      </address>
    </div>
    <div class="wordmark"><span class="wordmark__square"></span>Hadley &amp; Partners</div>
    <div class="footer-band"></div>
  </section>

  <section class="card card--back" aria-label="Card back">
    <div class="wordmark"><span class="wordmark__square"></span>Hadley &amp; Partners</div>
    <p class="website">www.hadleypartnersgroup.com</p>
  </section>
</body>
</html>
```